WordPress Website Design & Theme - The Meridale Bidding House

Need a WordPress design for an auction company wanting a responsive, simple and easy to use site.

Please keep in mind that the design will be built on a responsive WP theme.

Colors will be light or white and complimentary/highlight colors from the logo.

Industry/Entity Type

It Company

Number of Pages Required

1 page

Font styles to use
Serif
Sans Serif

Requirements
Must have
• Navigation - 1) Home 2) Auction Calendar 3) Auction Results 4) For Sale 5) Services 6)About Us 7) Contact Us
• A site they mention liking is http://www.quenbrookbids.example/
• Site will have full width slideshow 960px. Use stock real estate photo. Header will have logo (attached) and contact info:
• THE MERIDALE BIDDING HOUSE
• P.O. Box 582
• Gadsden, AL 35817
• PHONE: (800)615-3087 or (256)382-9061
• FAX: (256)382-5148
• EMAIL: info@meridale-bidding.example
• There will be no sidebar on the homepage. There can be 3 horizontal widgets for "featured Listings", Join Our Newsletter, and maybe a form like http://www.meridale-bidding.example/request_proposal.php. The "Upcoming Auctions" feature as is seen on http://www.quenbrookbids.example/ will be used (attached image).
• In the footer: contact info, social media (FB, twitter, RSS), affiliation logos (attached), perhaps smaller company logo, News & Events blog, and if room "Featured Auctions".
Nice to have
• Use of drop-down menus styling- 1) Live Auctions 2) Online Auctions - under the Auction Calendar tab

```html
<!DOCTYPE html>
<html lang="en">
<head>
<meta charset="utf-8">
<title>The Meridale Bidding House</title>
<link href="https://fonts.googleapis.com/css2?family=Roboto:wght@400;500;700&display=swap" rel="stylesheet">
<style>
:root{
  --red:#d9304f;
  --purple:#2e2a5e;
  --footer:#372f62;
  --ink:#333;
  --grey:#777;
  --line:#e4e4e8;
  --badge:#dcdcdc;
}
*{box-sizing:border-box;margin:0;padding:0}
html,body{width:791px;height:1200px;overflow:hidden;background:#fff;font-family:'Roboto',sans-serif;color:var(--ink)}
.page{position:relative;width:791px;height:1200px}
.abs{position:absolute}
.top-stripe{left:0;top:0;width:791px;height:4px;background:var(--red)}
.header-phone{left:114px;top:38px;display:flex;gap:8px;align-items:center}
.icon-ring{width:28px;height:28px;border:2px solid #333;border-radius:50%;display:flex;align-items:center;justify-content:center}
.header-phone small{display:block;font-size:8px;color:#444;letter-spacing:.3px}
.header-phone strong{display:block;font-size:15px;color:var(--red);font-weight:500;line-height:1}
.header-address{left:553px;top:38px;display:flex;gap:8px;align-items:center;font-size:10px;font-weight:500;color:#333;line-height:12px}
.brand{left:345px;top:22px;width:100px;text-align:center;font-weight:700;color:var(--red);font-size:13px;line-height:15px;display:flex;flex-direction:column;align-items:center;gap:4px}
.brand .dot{width:14px;height:14px;border-radius:50%;background:var(--purple)}
.nav{left:0;top:98px;width:791px;height:36px;background:var(--red);box-shadow:0 4px 8px rgba(0,0,0,.18)}
.nav ul{list-style:none;display:flex;position:absolute;left:127px;top:0;height:36px}
.nav li{font-size:8px;color:#fff;padding:0 15.5px;line-height:36px;font-weight:500;letter-spacing:.2px}
.nav li.active{background:var(--purple)}
.dropdown{left:181px;top:134px;width:105px;background:var(--purple);border-bottom:2px solid var(--red);z-index:3}
.dropdown div{font-size:8px;color:#fff;text-align:center;line-height:26px;font-weight:500}
.dropdown div+div{border-top:1px solid #463f78}
.slider{left:114px;top:134px;width:562px;height:219px;background:linear-gradient(120deg,#4a4a52 0%,#b89a86 40%,#e2c3ac 55%,#8a6c5f 80%,#3a3438 100%)}
.dots{left:355px;top:335px;display:flex;gap:11px}
.dots span{width:7px;height:7px;border-radius:50%;background:#fff}
.dots span.on{background:var(--red)}
.widget{top:371px;height:229px;background:#fff;box-shadow:0 2px 6px rgba(0,0,0,.15)}
.widget-head{height:43px;background:var(--purple);color:#fff;font-size:11px;font-weight:500;display:flex;align-items:center;padding-left:58px}
.widget-icon{position:absolute;left:-5px;top:-3px;width:46px;height:46px;border-radius:50%;background:var(--purple);border:3px solid var(--red);display:flex;align-items:center;justify-content:center}
.listing-photo{position:absolute;left:12px;top:52px;width:158px;height:95px;background:linear-gradient(160deg,#6b5a48,#c9b59b 50%,#e9e1d6)}
.listing-date{position:absolute;top:155px;width:100%;text-align:center;font-size:9.5px;font-weight:500;color:var(--purple)}
.listing-type{position:absolute;top:177px;left:20px;right:20px;text-align:center;font-size:9px;color:var(--red);line-height:9px}
.listing-addr{position:absolute;top:205px;width:100%;text-align:center;font-size:7.5px;color:#666}
.news-lead{position:absolute;left:14px;top:62px;font-size:10.5px;color:#333}
.news-red{position:absolute;left:14px;top:84px;width:160px;font-size:9px;color:var(--red);line-height:12px}
.news-note{position:absolute;left:14px;top:119px;width:160px;font-size:7.5px;color:#666;line-height:12px}
.field{position:absolute;height:24px;border:1px solid #d4d4d8;font-size:7.5px;color:#777;padding-left:10px;line-height:22px;background:#fff}
.btn{position:absolute;height:25px;background:var(--red);color:#fff;font-size:8px;font-weight:700;text-align:center;line-height:25px;border-radius:1px}
.divider{left:117px;top:631px;width:560px;height:1px;background:var(--line)}
.section-title{left:0;top:658px;width:791px;text-align:center;font-size:20px;font-weight:500;color:var(--purple)}
.auction-card{background:#fff;box-shadow:0 2px 6px rgba(0,0,0,.15)}
.painting{position:absolute;border:4px solid #8a6d3c;background:linear-gradient(180deg,#c9d8e4,#e8e4d6 60%,#9aa6a8)}
.date-badge{position:absolute;background:var(--badge);color:#777;text-align:center;font-weight:500}
.date-badge b{display:block;font-weight:500}
.date-badge.featured{background:var(--red);color:#fff}
.arrow-btn{width:27px;height:27px;border:1px solid #bbb;border-radius:50%;display:flex;align-items:center;justify-content:center;background:#fff}
.footer{left:0;top:927px;width:791px;height:218px;background:var(--footer)}
.footer h4{position:absolute;top:28px;font-size:11.5px;color:var(--red);font-weight:500}
.footer ul{position:absolute;top:55px;list-style:none}
.footer li{font-size:7.5px;color:#fff;line-height:16.4px;padding-left:10px;position:relative}
.footer li::before{content:"›";position:absolute;left:0;color:var(--red)}
.news-item{position:absolute;left:370px;width:146px;font-size:7.5px;color:#fff;line-height:16.5px;padding-left:16px}
.news-item em{font-style:normal;color:var(--red);display:block}
.contact-row{position:absolute;left:542px;display:flex;gap:9px;font-size:7.5px;color:#fff;line-height:18px}
.bottom-band{left:0;top:1145px;width:791px;height:55px;background:var(--red)}
.seal{left:345px;top:1120px;width:101px;height:101px;border-radius:50%;background:var(--purple);display:flex;align-items:center;justify-content:center;color:#fff;font-weight:700;font-size:11px;text-align:center;line-height:13px}
.copyright{left:115px;top:1180px;font-size:7.5px;color:#fff}
.follow{left:578px;top:1178px;display:flex;gap:10px;align-items:center;font-size:7.5px;color:#fff}
.follow span.s{width:9px;height:9px;border-radius:50%;background:#fff;opacity:.9}
</style>
</head>
<body>
<div class="page">
  <div class="abs top-stripe"></div>

  <div class="abs header-phone">
    <div class="icon-ring"><svg width="10" height="14" viewBox="0 0 10 14"><rect x="1" y="1" width="8" height="12" rx="1.5" fill="none" stroke="#d9304f" stroke-width="1.5"/><circle cx="5" cy="10.5" r=".9" fill="#d9304f"/></svg></div>
    <div><small>WE'RE OPEN 24 HRS A DAY</small><strong>(800)615-3087</strong></div>
  </div>

  <div class="abs brand"><span class="dot"></span><span>The Meridale<br>Bidding House</span></div>

  <div class="abs header-address">
    <div class="icon-ring"><svg width="10" height="14" viewBox="0 0 10 14"><path d="M5 13C5 13 1 8 1 5a4 4 0 0 1 8 0c0 3-4 8-4 8z" fill="none" stroke="#d9304f" stroke-width="1.5"/><circle cx="5" cy="5" r="1.4" fill="#d9304f"/></svg></div>
    <div>318, Linden Street<br>Gadsden, AL 35819</div>
  </div>

  <nav class="abs nav">
    <ul>
      <li>HOME</li><li class="active">AUCTION CALENDAR</li><li>AUCTION RESULTS</li><li>FOR SALE</li><li>SERVICES</li><li>ABOUT US</li><li>CONTACT US</li>
    </ul>
  </nav>

  <div class="abs slider" role="img" aria-label="Slideshow photo of bidders raising their hands at a live auction"></div>
  <div class="abs dropdown"><div>LIVE AUCTIONS</div><div>ONLINE AUCTIONS</div></div>
  <div class="abs dots"><span></span><span></span><span class="on"></span><span></span><span></span></div>

  <!-- Featured listings -->
  <section class="abs widget" style="left:114px;width:181px">
    <div class="widget-head">FEATURED LISTINGS</div>
    <div class="widget-icon"><svg width="20" height="20" viewBox="0 0 20 20"><rect x="7" y="2" width="9" height="5" rx="1" transform="rotate(45 11.5 4.5)" fill="#fff"/><rect x="2" y="11" width="9" height="2.5" transform="rotate(-45 6.5 12.2)" fill="#fff"/><rect x="2" y="16" width="8" height="2" fill="#fff"/></svg></div>
    <div class="listing-photo" role="img" aria-label="Photo of an auctioneer taking bids from a crowd"></div>
    <div class="listing-date">Thursday, February 18th, 2016</div>
    <div class="listing-type">Live On-Site Auction with Online Bidding.</div>
    <div class="listing-addr">227 Harvest Lane Millbrook, PA 18062</div>
  </section>

  <!-- Newsletter -->
  <section class="abs widget" style="left:305px;width:181px">
    <div class="widget-head">JOIN OUR NEWSLETTER</div>
    <div class="widget-icon"><svg width="20" height="20" viewBox="0 0 20 20"><path d="M2 10L18 3L14 17L10 12L16 5L8 11Z" fill="#fff"/></svg></div>
    <div class="news-lead">When you join our mailing list,</div>
    <div class="news-red">You will receive notices regarding upcoming auctions.</div>
    <div class="news-note">We value your privacy! We will not use your email address for other purposes.</div>
    <div class="field" style="left:13px;top:152px;width:150px">Email Address</div>
    <div class="btn" style="left:14px;top:183px;width:151px">SEND</div>
  </section>

  <!-- Proposal -->
  <section class="abs widget" style="left:495px;width:181px">
    <div class="widget-head">REQUEST A PROPOSAL</div>
    <div class="widget-icon"><svg width="20" height="20" viewBox="0 0 20 20"><rect x="2" y="5" width="16" height="11" rx="1" fill="#fff"/><path d="M2 6L10 11L18 6" fill="none" stroke="#2e2a5e" stroke-width="1.5"/></svg></div>
    <div class="field" style="left:14px;top:58px;width:151px">Full Name</div>
    <div class="field" style="left:14px;top:89px;width:151px">Phone Number</div>
    <div class="field" style="left:14px;top:119px;width:151px">Email Address</div>
    <div class="field" style="left:14px;top:148px;width:151px;height:30px">Property &nbsp;Description</div>
    <div class="btn" style="left:13px;top:183px;width:152px">SUBMIT</div>
  </section>

  <div class="abs divider"></div>
  <h2 class="abs section-title">UPCOMING AUCTIONS</h2>

  <div class="abs arrow-btn" style="left:54px;top:764px"><svg width="8" height="10"><path d="M6 1L2 5L6 9" fill="none" stroke="#d9304f" stroke-width="1.6"/></svg></div>
  <div class="abs arrow-btn" style="left:710px;top:764px"><svg width="8" height="10"><path d="M2 1L6 5L2 9" fill="none" stroke="#d9304f" stroke-width="1.6"/></svg></div>

  <div class="abs auction-card" style="left:113px;top:711px;width:172px;height:153px">
    <div class="painting" role="img" aria-label="Framed painting of a snowy village scene" style="left:49px;top:40px;width:75px;height:61px"></div>
    <div class="date-badge" style="left:65px;top:115px;width:43px;height:38px;padding-top:5px;font-size:13px;line-height:12px"><b>22</b><span style="font-size:6px;line-height:7px;display:block">MAR<br>2016</span></div>
  </div>
  <div class="abs auction-card" style="left:292px;top:697px;width:202px;height:180px">
    <div class="painting" role="img" aria-label="Framed painting of a winter farmhouse" style="left:57px;top:45px;width:90px;height:72px"></div>
    <div class="date-badge featured" style="left:73px;top:131px;width:56px;height:49px;padding-top:8px;font-size:16px;line-height:14px"><b>31</b><span style="font-size:8px;line-height:9px;display:block">MAR<br>2016</span></div>
  </div>
  <div class="abs auction-card" style="left:503px;top:711px;width:173px;height:153px">
    <div class="painting" role="img" aria-label="Framed painting of a snowy village scene" style="left:49px;top:40px;width:75px;height:61px"></div>
    <div class="date-badge" style="left:65px;top:115px;width:43px;height:38px;padding-top:5px;font-size:13px;line-height:12px"><b>22</b><span style="font-size:6px;line-height:7px;display:block">MAR<br>2016</span></div>
  </div>

  <footer class="abs footer">
    <h4 style="left:115px">NAVIGATION</h4>
    <ul style="left:115px"><li>Home</li><li>Auction Calendar</li><li>Auction Results</li><li>For Sale</li><li>Services</li><li>About Us</li><li>Contact Us</li></ul>
    <h4 style="left:235px">SERVICES</h4>
    <ul style="left:235px"><li>Our Services</li><li>Auctions &amp; Appraisals</li><li>Real Estate Listings</li><li>Real Estate Auctions</li><li>Appraisals</li><li>Senior Transitions</li><li>Cafe</li><li>Delivery</li></ul>
    <h4 style="left:370px">NEWS &amp; EVENTS</h4>
    <div class="news-item" style="top:54px"><em>➜&nbsp; Feb 18th, 2016</em>Live On-Site Auction with Online Bidding.</div>
    <div class="abs" style="left:370px;top:107px;width:146px;height:1px;background:#554c80"></div>
    <div class="news-item" style="top:117px"><em>➜&nbsp; Feb 18th, 2016</em>Live On-Site Auction with Online Bidding.</div>
    <h4 style="left:539px">CONTACT US</h4>
    <div class="contact-row" style="top:56px"><svg width="8" height="11" viewBox="0 0 10 14"><path d="M5 13C5 13 1 8 1 5a4 4 0 0 1 8 0c0 3-4 8-4 8z" fill="#d9304f"/></svg><div>THE MERIDALE BIDDING HOUSE<br>P.O. Box 582<br>Gadsden, AL 35817</div></div>
    <div class="contact-row" style="top:115px"><svg width="8" height="11" viewBox="0 0 10 14"><rect x="1" y="1" width="8" height="12" rx="1.5" fill="#d9304f"/></svg><div>(800)6153087 or (256)3829061</div></div>
    <div class="contact-row" style="top:133px"><svg width="9" height="11" viewBox="0 0 12 12"><rect x="1" y="3" width="10" height="8" fill="#d9304f"/><rect x="3" y="0" width="6" height="3" fill="#d9304f"/></svg><div>(256)3825148</div></div>
    <div class="contact-row" style="top:151px"><svg width="10" height="11" viewBox="0 0 12 12"><rect x="1" y="3" width="10" height="7" fill="#d9304f"/></svg><div>info@meridale-bidding.example</div></div>
  </footer>

  <div class="abs bottom-band"></div>
  <div class="abs seal"><span>The Meridale<br>Bidding House</span></div>
  <div class="abs copyright">© 2016. Brightlane Studio. Allrights Reserved</div>
  <div class="abs follow">Follow Us <span class="s"></span><span class="s"></span><span class="s"></span></div>
</div>
</body>
</html>
```